TRENDY & MODERN BUSINESS CARD DESIGN for Media Company *

I need a minimalistic - clean - modern and professional business card layout and design for MEDIA & PHOTOGRAPHY STUDIO.

We do NOT have a logo, and not really looking for one - but rather excellent typography and design. We would consider the 3 as a focal point.

We do personal and commercial photography.

Target Market(s)

Personal and commercial photography clientele

Contact Information for Business Card

ZUB size - from zub.com / size guidelines are enclosed in the brief

Font styles to use
Sans Serif

Colors
f78f20
eda3c7
cee9f5
0555a3
e667a6
fbf289

Requirements
Must have
• Clean lines - Modern layout
Nice to have
• All blue background as an option - use color palette in brief please.
Should not have
• Old fashion fonts and regular fonts.

```html
<!DOCTYPE html>
<html lang="en">
<head>
<meta charset="utf-8">
<title>Halvern Studio — Business Card</title>
<link rel="stylesheet" href="https://fonts.googleapis.com/css2?family=Roboto:wght@500&family=Work+Sans:wght@400&display=swap">
<style>
  :root {
    --backdrop: #d8d8d8;
    --card-light: #e3e3e3;
    --card-dark: #2f2f2f;
    --ink: #1d1d1d;
    --ink-inverse: #f4f4f4;
    --rule-light: #b9b9b9;
  }
  * { margin: 0; padding: 0; box-sizing: border-box; }
  html, body {
    width: 1200px; height: 965px; overflow: hidden;
    background: var(--backdrop);
  }
  .canvas { position: relative; width: 1200px; height: 965px; }
  .card {
    position: absolute; top: 159px; width: 383px; height: 668px;
  }
  .card--front { left: 186px; background: var(--card-light); color: var(--ink); }
  .card--back { left: 653px; background: var(--card-dark); color: var(--ink-inverse); }

  .brand { position: absolute; left: 36px; width: 314px; }
  .brand__name {
    font-family: "Roboto", sans-serif; font-weight: 500;
    font-size: 30px; letter-spacing: 2.6px; line-height: 1; white-space: nowrap;
  }
  .brand__tagline {
    font-family: "Work Sans", sans-serif; font-size: 17px;
    letter-spacing: 2.2px; margin-top: 19px; white-space: nowrap;
  }
  .card--front .brand { top: 48px; }
  .card--back .brand { top: 272px; }

  .block {
    position: absolute; left: 0; width: 100%; text-align: center;
    font-family: "Work Sans", sans-serif; font-size: 17.5px;
    letter-spacing: 2.3px; line-height: 26px;
  }
  .person__name {
    font-family: "Roboto", sans-serif; font-weight: 500;
    font-size: 24px; letter-spacing: 2.6px; line-height: 30px;
  }
  .person { top: 243px; }
  .address { top: 405px; }
  .contact { top: 487px; }
  .locations { top: 569px; }
  .divider {
    position: absolute; left: 0; width: 100%; height: 1px;
    background: var(--rule-light);
  }
  .divider--upper { top: 470px; }
  .divider--lower { top: 556px; }
</style>
</head>
<body>
<main class="canvas">
  <section class="card card--front" aria-label="Card front">
    <header class="brand">
      <div class="brand__name">HALVERN STUDIO</div>
      <div class="brand__tagline">Seeing Light.&nbsp; Shaping Stories.</div>
    </header>
    <div class="block person">
      <div class="person__name">MARISOL VANTERA</div>
      <div class="person__role">Founder &amp;Media Director</div>
    </div>
    <div class="block address">
      1450 Harbor Avenue<br>6th Floor Miami, FL 33178
    </div>
    <div class="divider divider--upper"></div>
    <div class="block contact">
      (305) 555-0148<br>marisol@halvernstudio.com
    </div>
    <div class="divider divider--lower"></div>
    <div class="block locations">
      Locations: Miami• New York •<br>Las Vegas • Cancun • Roma
    </div>
  </section>

  <section class="card card--back" aria-label="Card back">
    <header class="brand">
      <div class="brand__name">HALVERN STUDIO</div>
      <div class="brand__tagline">Seeing Light.&nbsp; Shaping Stories.</div>
    </header>
  </section>
</main>
</body>
</html>
```